Website Redesign Project Vault Quest Lodge

We are an escape room company located in Ashburn, Oregon. We currently have a website https://www.vaultquestlodge.example based upon html/bootstrap/javascript/php/mysql and I'd like to keep it that way. I'm looking for someone upgrade the front page so it is more informative, cleaner, quicker to load, and optimizes the space for full sale opportunities.

Target Market(s)

Corporate Clients, Families, Friends. All ages

Industry/Entity Type

Entertainment Industry

Coding

Number of Pages Required

3 page

Font styles to use
Other font styles liked:
• Similar to Facebook or Amazon

Requirements
Must have
• Must be mobile friendly. bootstrap. Lots of graphics (will provide) nice and easy to read fonts. Easy to read layout. Must look clean, fresh, exciting, and want to grab attention.
• Please visit my facebook page and website for more details. facebook.com/vaultquestlodge
Nice to have
• Same color as existing but open to options if they look nice.
Should not have
• Should not be wordpress or hard to modify.

```html
<!DOCTYPE html>
<html lang="en">
<head>
<meta charset="utf-8">
<title>Vault Quest Lodge</title>
<link rel="stylesheet" href="https://fonts.googleapis.com/css2?family=Lato:ital,wght@0,300;0,400;0,700;1,400;1,700&display=swap">
<style>
:root{
  --blue:#08a5e8;
  --ink:#222226;
  --dark:#403e3e;
  --page:#f6f6fb;
  --lav:#eceaf5;
  --white:#ffffff;
  --line:#d9d9e0;
}
*{box-sizing:border-box;margin:0;padding:0}
html,body{width:1200px;height:5137px;overflow:hidden;background:var(--page);font-family:'Lato',Arial,sans-serif;color:var(--ink)}
.site{position:relative;width:1200px;height:5137px;overflow:hidden}
.abs{position:absolute}
/* header */
.header{left:0;top:0;width:1200px;height:76px;background:var(--white)}
.brand{left:0;top:0;width:226px;height:118px;background:#0b0b0d;z-index:3;display:flex;align-items:center;justify-content:center;gap:10px;color:var(--blue);font-weight:700;font-size:19px;letter-spacing:.5px}
.brand-mark{width:14px;height:14px;background:var(--blue)}
.nav{left:312px;top:34px;display:flex;gap:28px;font-size:11px;letter-spacing:1.2px;text-transform:uppercase}
.btn-outline{border:2px solid var(--ink);background:var(--white);font-size:10px;letter-spacing:1.2px;text-transform:uppercase;display:flex;align-items:center;justify-content:center}
.nav-book{left:988px;top:22px;width:118px;height:36px;font-size:10px}
.hero{left:0;top:76px;width:1200px;height:678px;background:linear-gradient(160deg,#3a6fb0,#2c4f86 45%,#6a5a58)}
/* rooms */
.block-blue{background:var(--blue)}
.photo{background:#999}
.room-title{font-size:27px;font-weight:400}
.room-title::after{content:"";display:block;width:56px;height:3px;background:currentColor;margin-top:14px}
.room-text{font-size:14px;line-height:23px;font-weight:400}
.btn-small{background:#151515;color:var(--white);font-size:11px;font-weight:700;letter-spacing:1px;padding:5px 10px;display:inline-block}
.btn-small.on-dark{border:1px solid var(--white)}
.bank-card{left:826px;top:1188px;width:260px;height:634px;border:2px solid #888;background:var(--white)}
/* corporate */
.corp-band{left:0;top:2248px;width:1200px;height:474px;background:linear-gradient(180deg,#2e3a4e,#4b5566 60%,#6c7480)}
.corp-title{left:0;top:2312px;width:1200px;text-align:center;color:var(--white);font-size:36px;font-weight:300}
.corp-contact{left:524px;top:2374px;width:154px;height:40px;border:2px solid var(--white);border-radius:20px;color:var(--white);font-size:12px;letter-spacing:1.5px;display:flex;align-items:center;justify-content:center;text-transform:uppercase}
.corp-card{top:2456px;width:320px;height:264px;background:var(--white);padding:0 44px;text-align:center}
.corp-card svg{margin-top:40px}
.corp-card h3{color:var(--blue);font-size:20px;font-weight:400;line-height:25px;margin-top:12px}
.corp-card p{font-size:13px;line-height:20px;text-align:left;margin-top:14px}
.players{font-size:14px;text-align:left;margin-top:18px}
.players b{font-weight:700}
.quote{left:180px;top:2930px;width:842px;height:148px;border:2px solid var(--ink);padding:26px 90px;text-align:center;font-style:italic;font-weight:700;font-size:13.5px;line-height:22px}
.quote-btn{left:560px;top:3054px;width:154px;height:40px;border-radius:20px;font-size:13px;font-weight:700}
/* birthday */
.bday h2{font-size:27px;font-weight:400}
.bday-text{font-size:14px;line-height:22px}
.bday-item{display:flex;gap:14px;font-size:14px;line-height:22px}
.bday-item svg{flex:none}
.bday-note{font-style:italic;font-weight:700;font-size:14px;line-height:22px}
.round-btn{border-radius:20px;font-weight:700;font-size:13px}
/* faq */
.faq{left:0;top:3814px;width:1200px;height:712px;background:var(--lav)}
.faq-intro{left:270px;top:3930px;width:660px;text-align:center;font-size:16px;line-height:26px}
.faq-dash{left:574px;top:4022px;width:52px;height:4px;background:var(--ink)}
.faq-row{width:420px;height:46px;background:var(--white);display:flex;align-items:center;font-size:14px;box-shadow:0 2px 4px rgba(0,0,0,.06)}
.faq-plus{width:46px;height:46px;background:var(--blue);display:flex;align-items:center;justify-content:center;margin-right:24px}
/* contact */
.contact-band{left:0;top:4526px;width:1200px;height:514px;background:var(--blue)}
.form-panel{left:92px;top:4526px;width:498px;height:514px;background:var(--white)}
.call{left:134px;top:4588px;font-size:26px;line-height:30px;font-weight:400}
.field{left:132px;width:416px;height:42px;border:1px solid var(--line);font-size:11px;padding:14px;color:#555}
.send{left:128px;top:4974px;width:156px;height:38px;font-size:12px;font-weight:700}
.loc-word{left:636px;top:4660px;width:100px;height:300px;display:flex;align-items:center;justify-content:center}
.loc-word span{transform:rotate(-90deg);color:var(--white);font-size:46px;letter-spacing:6px;font-weight:400;white-space:nowrap}
.loc-info{left:758px;top:4658px;color:var(--white)}
.loc-info h3{font-size:33px;font-weight:400}
.loc-info p{font-size:17px;line-height:27px}
.footer{left:0;top:5076px;width:1200px;text-align:center;font-size:15px}
</style>
</head>
<body>
<div class="site">

  <header>
    <div class="abs header"></div>
    <div class="abs brand"><span class="brand-mark"></span>Vault Quest Lodge</div>
    <nav class="abs nav"><span>Escape Rooms</span><span>Special Events</span><span>Locations</span><span>How It Works</span><span>Contact Us</span></nav>
    <div class="abs btn-outline nav-book">Book Now</div>
  </header>

  <div class="abs hero" role="img" aria-label="Photo of a large family group posing together in the lobby"></div>

  <!-- Elevator -->
  <div class="abs block-blue" style="left:196px;top:754px;width:310px;height:226px"></div>
  <div class="abs photo" style="left:232px;top:790px;width:358px;height:474px;background:linear-gradient(180deg,#3a3330,#6d6660 55%,#a8773e)" role="img" aria-label="Photo of a freight elevator with a folding gate"></div>
  <div class="abs" style="left:666px;top:904px;width:340px">
    <h2 class="room-title">Elevator</h2>
    <p class="room-text" style="margin-top:36px">The main elevators are down so you'll need to take the freight elevator to the top floor if you want to get your award. The last celebrity that attempted to do so wasn't so lucky.</p>
    <span class="btn-small" style="margin-top:10px">Book Now</span>
  </div>

  <!-- Bank Heist -->
  <div class="abs bank-card"></div>
  <div class="abs photo" style="left:828px;top:1190px;width:256px;height:330px;background:radial-gradient(circle,#3a3e48,#8a8a8c 80%,#d8d8d8)" role="img" aria-label="Photo of a heavy steel vault door"></div>
  <div class="abs" style="left:852px;top:1566px;width:210px">
    <h2 class="room-title">Bank Heist</h2>
    <p class="room-text" style="margin-top:26px">With your family held hostage, the mob gave you one choice - rob the bank in exchange for their freedom or its goodbyes forever.</p>
    <span class="btn-small" style="margin-top:12px">Book Now</span>
  </div>

  <!-- Candy Shop -->
  <div class="abs" style="left:0;top:1336px;width:326px;height:330px;background:var(--dark)"></div>
  <div class="abs photo" style="left:326px;top:1336px;width:434px;height:330px;background:linear-gradient(180deg,#a53030 0,#a53030 22%,#b7bedb 22%,#e4e2ec 75%,#f1f1f3)" role="img" aria-label="Photo of candy-filled glass tubes in a striped room"></div>
  <div class="abs" style="left:98px;top:1422px;width:200px;color:var(--white)">
    <h2 class="room-title">Candy Shop</h2>
    <p class="room-text" style="margin-top:20px">With all of the candy right before your eyes, find the golden ticket and win the prize!</p>
    <span class="btn-small on-dark" style="margin-top:12px">Book Now</span>
  </div>

  <!-- Jail Break -->
  <div class="abs photo" style="left:92px;top:1726px;width:622px;height:428px;background:linear-gradient(180deg,#2c2e30,#4c4a44 40%,#d9582a 75%,#e46a34)" role="img" aria-label="Photo of a group wearing orange jumpsuits"></div>
  <div class="abs block-blue" style="left:638px;top:1894px;width:304px;height:260px"></div>
  <div class="abs" style="left:682px;top:1978px;width:240px;color:var(--white)">
    <h2 class="room-title">Jail Break</h2>
    <p class="room-text" style="margin-top:18px">One Guard, One Goal: get out.</p>
    <span class="btn-small" style="margin-top:12px">Book Now</span>
  </div>

  <!-- Corporate -->
  <div class="abs corp-band" role="img" aria-label="Photo of a banquet hall with set tables"></div>
  <h2 class="abs corp-title">Corporate Events</h2>
  <div class="abs corp-contact">Contact Us</div>

  <div class="abs corp-card" style="left:92px">
    <svg width="44" height="44" viewBox="0 0 44 44" fill="none" stroke="#08a5e8" stroke-width="2"><path d="M6 6h16l16 16-16 16L6 22z"/><circle cx="14" cy="14" r="3"/></svg>
    <h3>On-site multi-<br>room packages</h3>
    <p>Come, enjoy, relax in our multi-room escape room facility with your team. With four different rooms to choose from we are able to accommodate up to 30 people in a single hour.</p>
  </div>
  <div class="abs corp-card" style="left:440px">
    <svg width="44" height="44" viewBox="0 0 44 44" fill="none" stroke="#08a5e8" stroke-width="2"><path d="M6 6h16l16 16-16 16L6 22z"/><circle cx="14" cy="14" r="3"/></svg>
    <h3>Off-site Hot Seat<br>Escape Room package</h3>
    <p>Enjoy a 2 or 4 hour escape room in the new thrilling Hot Seat challenge! Each player is given two minutes to solve the challenge at hand before they go up in smoke! Can you do it?</p>
    <p class="players"><b>Number of Players</b>: 20 to 100</p>
  </div>
  <div class="abs corp-card" style="left:788px">
    <svg width="44" height="44" viewBox="0 0 44 44" fill="none" stroke="#08a5e8" stroke-width="2"><path d="M6 6h16l16 16-16 16L6 22z"/><circle cx="14" cy="14" r="3"/></svg>
    <h3 style="margin-top:6px">Off-site Custom<br>Escape Room Package</h3>
    <p>Enjoy a customized escape room game to fit the theme you'd like to celebrate. You and your team will come in to work or what seems to be a normal work day until they arrive in an immersive experience for all to enjoy. Each game is customized and includes live actors.</p>
    <p class="players"><b>Number of Players</b>: 30+</p>
  </div>

  <div class="abs quote">Vault Quest Lodge is the perfect place to gather groups of colleagues, friends, or family and experience the latest entertainment in town. Simply complete the form below and our specialist will contact you for further details. Group pricing is available on group parties.</div>
  <div class="abs btn-outline quote-btn">Book Now</div>

  <!-- Birthday -->
  <div class="abs block-blue" style="left:570px;top:3180px;width:250px;height:280px"></div>
  <div class="abs photo" style="left:614px;top:3220px;width:586px;height:594px;background:linear-gradient(160deg,#f2b8b6,#ee9d9b 60%,#e0574b)" role="img" aria-label="Photo of a laughing child with a birthday cake under falling confetti"></div>
  <section class="abs bday" style="left:92px;top:3218px;width:400px">
    <h2>Birthday Parties</h2>
    <p class="bday-text" style="margin-top:14px">Celebrate this year in style by treating your family with an escape room birthday package. You and your loved ones have the choice of four escape rooms and will enjoy a private party afterwards in our party room. Either of these packages will be sure to satisfy your needs.</p>
    <div class="bday-item" style="margin-top:34px">
      <svg width="34" height="34" viewBox="0 0 34 34" fill="none" stroke="#08a5e8" stroke-width="1.6"><circle cx="17" cy="17" r="15"/><path d="M14 11l6 6-6 6"/></svg>
      <p>A private escape room event with party room pizza and soda.<br><b>Add just $150 to your escape room.</b></p>
    </div>
    <div class="bday-item" style="margin-top:26px">
      <svg width="34" height="34" viewBox="0 0 34 34" fill="none" stroke="#08a5e8" stroke-width="1.6"><circle cx="17" cy="17" r="15"/><path d="M14 11l6 6-6 6"/></svg>
      <p>A private escape room event with a party room rental. Bring your own food.<br>Add just $125.</p>
    </div>
    <p class="bday-note" style="margin-top:28px;padding-left:6px">Note: A $50 cleaning fee applies to all parties who don't clean after themselves</p>
  </section>
  <div class="abs btn-outline round-btn" style="left:92px;top:3706px;width:152px;height:40px">Contact Us</div>

  <!-- FAQ -->
  <div class="abs faq"></div>
  <p class="abs faq-intro">An escape room is a themed environment where you and your friends must work together to complete the objectives through solving puzzles before time runs out. Most missions will lock you in while some of our missions do not.</p>
  <div class="abs faq-dash"></div>

  <div class="abs" style="left:176px;top:4098px;display:grid;grid-template-columns:420px 420px;column-gap:18px;row-gap:18px">
    <div class="faq-row"><span class="faq-plus"><svg width="16" height="16"><path d="M8 1v14M1 8h14" stroke="#fff" stroke-width="2"/></svg></span>How do I make a reservation?</div>
    <div class="faq-row"><span class="faq-plus"><svg width="16" height="16"><path d="M8 1v14M1 8h14" stroke="#fff" stroke-width="2"/></svg></span>How do I make a reservation?</div>
    <div class="faq-row"><span class="faq-plus"><svg width="16" height="16"><path d="M8 1v14M1 8h14" stroke="#fff" stroke-width="2"/></svg></span>I'm pregnant, can I participate?</div>
    <div class="faq-row"><span class="faq-plus"><svg width="16" height="16"><path d="M8 1v14M1 8h14" stroke="#fff" stroke-width="2"/></svg></span>I'm pregnant, can I participate?</div>
    <div class="faq-row"><span class="faq-plus"><svg width="16" height="16"><path d="M8 1v14M1 8h14" stroke="#fff" stroke-width="2"/></svg></span>What is the cancellation policy?</div>
    <div class="faq-row"><span class="faq-plus"><svg width="16" height="16"><path d="M8 1v14M1 8h14" stroke="#fff" stroke-width="2"/></svg></span>What is the cancellation policy?</div>
    <div class="faq-row"><span class="faq-plus"><svg width="16" height="16"><path d="M8 1v14M1 8h14" stroke="#fff" stroke-width="2"/></svg></span>Do I have to sign a liability waiver?</div>
    <div class="faq-row"><span class="faq-plus"><svg width="16" height="16"><path d="M8 1v14M1 8h14" stroke="#fff" stroke-width="2"/></svg></span>Do I have to sign a liability waiver?</div>
    <div class="faq-row"><span class="faq-plus"><svg width="16" height="16"><path d="M8 1v14M1 8h14" stroke="#fff" stroke-width="2"/></svg></span>What time should we arrive?</div>
    <div class="faq-row"><span class="faq-plus"><svg width="16" height="16"><path d="M8 1v14M1 8h14" stroke="#fff" stroke-width="2"/></svg></span>What time should we arrive?</div>
  </div>

  <!-- Contact -->
  <div class="abs contact-band"></div>
  <div class="abs form-panel"></div>
  <p class="abs call">Call <b>555 014 2290</b><br>or send us a message.</p>
  <div class="abs field" style="top:4670px">Enter your name</div>
  <div class="abs field" style="top:4730px">Enter your email</div>
  <div class="abs field" style="top:4790px">Enter your phone</div>
  <div class="abs field" style="top:4850px;height:86px">We'd love to hear from you. We'll get back to you immediately.</div>
  <div class="abs btn-outline send round-btn">Send Message</div>

  <div class="abs loc-word"><span>LOCATION</span></div>
  <div class="abs loc-info">
    <h3>Oregon</h3>
    <p style="margin-top:22px">1180 Lantern Ridge Way, Suite 12<br>Millbrook, OR 97099<br>(555) 014 2290</p>
    <p style="margin-top:26px">HOURS:<br>Wednesday - Friday: 3pm - 9pm<br>Saturday: 10am - 10pm<br>Sunday: 10am - 8:30pm.</p>
  </div>

  <footer class="abs footer">© 2019 Vault Quest Lodge. All Rights Reserved</footer>
</div>
</body>
</html>
```